White Paper and One-Page Advertisement for TELVAMORE-QX

I need both documents to be better formatted and designed so they look professional, not something someone with mediocre word skills put together. They will go out to 1000s of industry professionals, and they need to look sharp. I need them to have my company's color palate logo, and branding on it similar to how it is now, but better. Please do not change any of the written content, but it can be arranged in any other format you think is better. Smart art and things i've already used can be omitted in favor of better designs. The developer is free to use their creativity. White paper should not be longer than the three pages unless necessary.

Target Market(s)

Life Sciences supply chain professionals

Colors
33b8a4
0592cd
9bcb3c
fbee3e
3277b5

Requirements
Must have
• Must be professional looking and not look like something done in word. Please use the color palate as seen on the documents.
Should not have
• Any changes to the written content.

```html
<!DOCTYPE html>
<html lang="en">
<head>
<meta charset="utf-8">
<title>TELVAMORE-QX One-Page Advertisement</title>
<link href="https://fonts.googleapis.com/css2?family=Rubik:wght@400;500;700&family=Montserrat:wght@400;500;600&display=swap" rel="stylesheet">
<style>
:root{
  --teal:#1b8074;
  --teal-dark:#136a60;
  --green:#8cc63f;
  --green-light:#a9d65a;
  --ink:#2a2a2a;
  --white:#ffffff;
}
*{margin:0;padding:0;box-sizing:border-box}
html,body{width:963px;height:1200px;overflow:hidden;background:var(--white)}
body{font-family:"Montserrat",sans-serif;color:var(--ink);position:relative}
.abs{position:absolute}
.hero-art{left:0;top:0;width:963px;height:440px}
.brand-lockup{left:60px;top:40px;width:330px;display:flex;flex-direction:column;align-items:center;gap:14px}
.brand-dot{width:86px;height:86px;border-radius:50%;border:6px solid var(--teal)}
.brand-name{font-family:"Rubik",sans-serif;font-weight:700;font-size:40px;color:var(--teal);letter-spacing:1px}
.intro{left:32px;top:206px;width:420px}
.intro h1{font-family:"Rubik",sans-serif;font-weight:700;font-size:28px;color:var(--teal)}
.intro h1 span{color:var(--green)}
.intro p{font-size:16px;line-height:21px;margin-top:2px}
.mission{left:32px;top:302px;width:420px;color:var(--white);font-family:"Rubik",sans-serif;font-size:19.5px;line-height:26px;font-weight:400}
.mission em{font-style:normal;color:var(--green)}
.section-title{font-family:"Rubik",sans-serif;font-size:24px;color:var(--teal);display:flex;align-items:center;gap:12px}
.section-title b{color:var(--green);font-weight:700}
.section-title i{display:block;width:100px;height:3px;background:var(--green)}
.platform{left:28px;top:478px;width:490px}
ul.dots{list-style:none}
ul.dots li{position:relative;padding-left:26px;font-size:14.5px;line-height:19px;margin-bottom:9px;text-align:justify}
ul.dots li::before{content:"";position:absolute;left:4px;top:6px;width:7px;height:7px;border-radius:50%;background:var(--green)}
.platform ul{margin-top:16px}
.steps{left:32px;top:647px;width:482px;display:flex;flex-direction:column;gap:4px}
.step{position:relative;height:40px;border-radius:0 16px 16px 0;margin-left:12px;padding-left:36px;display:flex;align-items:center;color:var(--white);font-family:"Rubik",sans-serif;font-weight:700;font-size:19.5px;line-height:20px}
.step.tall{height:52px}
.step.green{background:var(--green)}
.step.teal{background:var(--teal)}
.step .chev{position:absolute;left:-12px;top:50%;transform:translateY(-50%);width:32px;height:32px;border-radius:50%;border:2px solid var(--white);display:flex;align-items:center;justify-content:center}
.step.green .chev{background:var(--teal)}
.step.teal .chev{background:var(--green)}
.compliance{left:28px;top:852px;width:490px}
.benefits-panel{left:541px;top:427px;width:422px;height:478px}
.benefits{left:573px;top:478px;width:352px;color:var(--white)}
.benefits .section-title{color:var(--white)}
.benefits .section-title i{background:var(--teal)}
.benefits ul{margin-top:26px}
.benefits li{font-size:16px;line-height:20px;margin-bottom:12px;color:var(--teal-dark)}
.benefits li::before{background:var(--white)}
.promise{left:39px;top:970px;width:886px;height:108px}
.promise-title{left:0;top:975px;width:963px;text-align:center;font-family:"Rubik",sans-serif;font-size:27px;color:var(--teal)}
.promise-title b{color:var(--green)}
.promise-text{left:100px;top:1019px;width:763px;text-align:center;font-size:17.5px;line-height:22px}
.footer{left:0;top:1124px;width:963px;height:76px;background:linear-gradient(90deg,var(--teal-dark),var(--teal) 50%,var(--teal-dark));border-top:3px solid var(--green)}
.touch{left:380px;top:1109px;width:204px;height:33px;border-radius:17px;background:var(--green);color:var(--white);font-family:"Rubik",sans-serif;font-weight:700;font-size:19.5px;display:flex;align-items:center;justify-content:center;letter-spacing:.5px}
.contact-row{left:0;top:1152px;width:963px;height:36px;display:flex;align-items:center;font-size:18px;color:var(--white)}
.web{background:var(--white);height:36px;width:328px;border-radius:0 18px 18px 0;display:flex;align-items:center;gap:8px;padding-left:24px;color:var(--green);font-family:"Rubik",sans-serif;font-weight:700;font-size:18px}
.mail{display:flex;align-items:center;gap:10px;margin-left:24px}
.paper{display:flex;align-items:center;gap:10px;margin-left:20px}
.paper b{font-family:"Rubik",sans-serif;font-weight:700}
</style>
</head>
<body>

<svg class="abs hero-art" viewBox="0 0 963 440" aria-hidden="false">
  <polygon points="0,292 500,292 560,413 0,413" fill="var(--teal)"/>
  <polygon points="270,413 602,413 602,427 285,427" fill="var(--green)"/>
  <circle cx="740" cy="215" r="250" fill="var(--green)"/>
  <path d="M490 120 L470 190 L500 180" fill="var(--green)"/>
  <path d="M575 0 A250 250 0 0 0 503 110" stroke="var(--teal)" stroke-width="16" fill="none"/>
  <g role="img" aria-label="Photo of smiling people at a traditional ceremony, one tying a cord on another's wrist">
    <circle cx="748" cy="205" r="232" fill="url(#photoTone)"/>
  </g>
  <defs>
    <linearGradient id="photoTone" x1="0" y1="0" x2="1" y2="1">
      <stop offset="0" stop-color="#6a3f2a"/>
      <stop offset=".5" stop-color="#a07a5e"/>
      <stop offset="1" stop-color="#3c5a6a"/>
    </linearGradient>
  </defs>
</svg>

<div class="abs brand-lockup">
  <div class="brand-dot"></div>
  <div class="brand-name">TELVAMORE-QX</div>
</div>

<div class="abs intro">
  <h1>TELVAMORE<span>-QX</span></h1>
  <p>aspires to change the waste and risk paradigm<br>in the life science industry.</p>
</div>

<p class="abs mission">We strive to make companies better stewards of their dollars and our environment to transfer benefit to them...<em>THE PATIENT</em></p>

<svg class="abs benefits-panel" viewBox="0 0 422 478" aria-hidden="true">
  <defs>
    <linearGradient id="panelTone" x1="0" y1="0" x2="0" y2="1">
      <stop offset="0" stop-color="#8cc63f"/>
      <stop offset="1" stop-color="#b2dc6a"/>
    </linearGradient>
  </defs>
  <path d="M0 0 H422 V0 L397 0 V430 Q397 454 373 454 H231 Q231 478 199 478 Q167 478 167 454 H24 Q0 454 0 430 Z" fill="url(#panelTone)"/>
</svg>

<section class="abs platform">
  <h2 class="section-title">OUR <b>PLATFORM</b><i></i></h2>
  <ul class="dots">
    <li>A multi-vendor marketplace for the life science community to transact pre-market and after-market materials and equipment</li>
    <li>Researchers, manufactures, and original suppliers can create an account to buy, sell, or donate materials</li>
  </ul>
</section>

<div class="abs steps">
  <div class="step green"><span class="chev"><svg width="12" height="14" viewBox="0 0 12 14"><path d="M3 1 L9 7 L3 13" stroke="#fff" stroke-width="2.5" fill="none"/></svg></span>Authentication&nbsp; and Terms of Quality</div>
  <div class="step teal"><span class="chev"><svg width="12" height="14" viewBox="0 0 12 14"><path d="M3 1 L9 7 L3 13" stroke="#fff" stroke-width="2.5" fill="none"/></svg></span>Set up store</div>
  <div class="step green tall"><span class="chev"><svg width="12" height="14" viewBox="0 0 12 14"><path d="M3 1 L9 7 L3 13" stroke="#fff" stroke-width="2.5" fill="none"/></svg></span>Seamlessly trasnact and request for<br>inornation</div>
  <div class="step teal"><span class="chev"><svg width="12" height="14" viewBox="0 0 12 14"><path d="M3 1 L9 7 L3 13" stroke="#fff" stroke-width="2.5" fill="none"/></svg></span>Check Out and Sign</div>
</div>

<ul class="abs dots compliance">
  <li>Part 11 compliant signature and authentication</li>
  <li>Leverages industry auditing skills to facilitate compliant and transparent transactions</li>
  <li>Some of the best and industry vendors and software used</li>
</ul>

<section class="abs benefits">
  <h2 class="section-title"><b style="color:var(--white)">BENEFITS</b><i></i></h2>
  <ul class="dots">
    <li>Reduce write-offs by selling excess and obsolete materials, equipment, spare parts, etc.</li>
    <li>Buy quality materials at a reduced price.</li>
    <li>Market materials if an original supplier</li>
    <li>Donate material to researchers</li>
    <li>Acquire donated materials</li>
    <li>Collaborate and consort to reduce supply chain risk such as mutual aid agreements, joint supplier audits, etc.</li>
  </ul>
</section>

<svg class="abs promise" viewBox="0 0 886 108" aria-hidden="true">
  <path d="M95 22 H300 M650 22 H860 Q880 22 880 42 V80 Q880 90 870 96 M820 106 H20 Q6 106 6 92 V42 Q6 30 16 26" stroke="var(--green)" stroke-width="1.5" stroke-dasharray="5 4" fill="none"/>
  <text x="28" y="62" font-family="Rubik,sans-serif" font-weight="700" font-size="78" fill="#cfe6a8">&#8220;</text>
  <text x="796" y="140" font-family="Rubik,sans-serif" font-weight="700" font-size="78" fill="#cfe6a8">&#8221;</text>
</svg>
<h2 class="abs promise-title">OUR <b>PROMISE</b></h2>
<p class="abs promise-text">A greener, more cost-efficient, and quality driven supply chain through a collaborative life sciences marketplace.</p>

<footer class="abs footer"></footer>
<div class="abs touch">GET IN TOUCH</div>
<div class="abs contact-row">
  <div class="web">
    <svg width="20" height="20" viewBox="0 0 20 20"><g stroke="var(--teal)" stroke-width="1.5" fill="none"><circle cx="10" cy="10" r="8.5"/><ellipse cx="10" cy="10" rx="4" ry="8.5"/><path d="M1.5 10 H18.5 M3 5.5 H17 M3 14.5 H17"/></g></svg>
    www.telvamoreqx.com
  </div>
  <div class="mail">
    <svg width="22" height="16" viewBox="0 0 22 16"><rect x="1" y="1" width="20" height="14" fill="none" stroke="var(--green)" stroke-width="1.6"/><path d="M1 1 L11 9 L21 1" fill="none" stroke="var(--green)" stroke-width="1.6"/></svg>
    info@telvamoreqx.com
  </div>
  <div class="paper">
    <svg width="18" height="22" viewBox="0 0 18 22"><path d="M1 1 H12 L17 6 V21 H1 Z" fill="none" stroke="var(--green)" stroke-width="1.6"/><path d="M4 9 H13 M4 13 H13 M4 17 H10" stroke="var(--green)" stroke-width="1.4"/></svg>
    <span>Read our <b>WHITE PAPER</b></span>
  </div>
</div>

</body>
</html>
```